lighting products eshop web site

We need a brand new ecommerce website (only psd files for the layout) , that will sell professional lighting products in Greek territory.
Please check the sister site www.lampiroxa.gr to get an idea of the products, they will be similar, actually like the products under the menu category "ΕΠΑΓΓΕΛΜΑΤΙΚΑ".
We would like the same philosophy as far as concern the menu structure, namely the menu categories/subcategories shall be actually the products
categories/subcategories, however the menu items shall be presented in a different, more sophisticated way. As far as concern the website layout, we need a minimal, elegant
and contemporary approach that will highlight the products in a perfect manner. We prefer the white color as the main website (background) color and discrete use of brand logo colors.
That is the main idea, awaiting your personal proposal according to the aforementioned requirements
Technically speaking we use bootstrap framework in terms of design meaning 12cols with max width 1170px.
The website will be a joomla - virtuemart website

For images please use some from lampiroxa.gr
For text use any text - just to show me the space.

Industry/Entity Type

It Professional

Number of Pages Required

3 page

Font styles to use
Sans Serif

Colors
00a990
ec1f27

Requirements
Must have
• I need 4 psd pages for the website
• 1. Start page
• 2. Category page
• 3. Product details page
• 4. blog page
Nice to have
• leave designer to choose the best

```html
<!DOCTYPE html>
<html lang="en">
<head>
<meta charset="utf-8">
<title>Lampiroxa – Product details</title>
<link rel="stylesheet" href="https://fonts.googleapis.com/css2?family=Montserrat:wght@300;400;500;600;700&family=Oswald:wght@500&family=Open+Sans:ital,wght@0,400;0,600;1,400&display=swap">
<style>
:root{
  --red:#ec1f27;
  --teal:#00a990;
  --ink:#222;
  --text:#555;
  --muted:#888;
  --line:#e5e5e5;
  --soft:#f2f2f2;
  --footer:#1f1f1f;
  --footer-bar:#2b2b2b;
  --footer-text:#9a9a9a;
  --hero:#8fabc9;
}
*{margin:0;padding:0;box-sizing:border-box}
html,body{width:1200px;height:2594px;overflow:hidden;background:#fff}
body{position:relative;font-family:"Montserrat",sans-serif;color:var(--text)}
.abs{position:absolute}
a{color:inherit;text-decoration:none}

/* top bar */
.topbar{left:0;top:0;width:1200px;height:31px;background:var(--red);color:#fff;font:400 11.5px "Open Sans",sans-serif}
.topbar .address{left:145px;top:8px}
.topbar .phone{right:144px;top:8px}

/* header */
.search{left:144px;top:55px;width:266px;height:28px;border:1px solid #ddd;display:flex;font:400 11px "Open Sans",sans-serif;color:#aaa}
.search .scope{width:52px;border-right:1px solid #ddd;display:flex;align-items:center;justify-content:center;gap:6px;color:#333}
.search .field{flex:1;padding-left:10px;display:flex;align-items:center;justify-content:space-between;padding-right:10px}
.header-links{top:63px;font:400 11px "Montserrat",sans-serif;color:#333;letter-spacing:.5px}
.cart-total{left:1015px;top:62px;font:500 13px "Montserrat",sans-serif;color:#333}
.cart-badge{left:993px;top:55px;width:15px;height:15px;border-radius:50%;background:var(--red);color:#fff;font:600 9px "Montserrat",sans-serif;text-align:center;line-height:15px}
.brand{left:0;width:1200px;top:136px;text-align:center;font:300 54px "Montserrat",sans-serif;letter-spacing:9px;color:var(--red)}

/* nav */
.main-nav{left:0;top:228px;width:1200px;height:52px;border-top:1px solid var(--line);border-bottom:1px solid var(--line)}
.main-nav a{position:absolute;top:17px;font:700 13.5px "Montserrat",sans-serif;letter-spacing:2px;color:#111}
.main-nav a.active{color:var(--teal)}
.main-nav .sep{position:absolute;top:20px;width:1px;height:12px;background:#ddd}

/* hero */
.hero{left:0;top:280px;width:1200px;height:318px;background:linear-gradient(90deg,#9bb4cf 0%,var(--hero) 45%,#86a6c6 100%)}
.hero h1{position:absolute;left:522px;top:80px;color:#fff;font:700 38px/52px "Montserrat",sans-serif;letter-spacing:6px}

/* breadcrumb */
.breadcrumb{left:0;top:598px;width:1200px;height:47px;background:var(--soft);font:400 10.5px "Montserrat",sans-serif;color:var(--muted)}
.breadcrumb span{position:absolute;right:146px;top:17px}
.breadcrumb .current{color:var(--teal);font-weight:400}

/* gallery */
.main-photo{left:175px;top:690px;width:380px;height:390px;background:radial-gradient(circle at 50% 42%,#f4f4f4 0%,#e8e8e8 45%,#fff 72%)}
.thumb{width:94px;height:89px;border:1px solid #ccc;background:radial-gradient(circle at 50% 45%,#ececec 0%,#fff 70%)}
.arrow{width:14px;height:24px}

/* product info */
.product-title{left:615px;top:697px;width:405px;font:400 23px/29px "Montserrat",sans-serif;color:#222}
.red-rule{height:3px;background:var(--red)}
.price{left:615px;top:812px;color:#111;font-family:"Montserrat",sans-serif;font-weight:700}
.price .cur{font-size:22px}
.price .int{font-size:42px}
.price .dec{font-size:24px}
.qty{left:615px;top:889px;width:72px;height:33px;border:1px solid #999;font:500 11px "Montserrat",sans-serif;color:#333;display:flex;align-items:center;letter-spacing:1px}
.qty span{padding-left:12px;flex:1}
.qty i{width:18px;height:100%;border-left:1px solid #ccc;display:flex;align-items:center;justify-content:center}
.add-cart{left:697px;top:889px;width:150px;height:33px;background:var(--red);color:#fff;font:700 11.5px "Montserrat",sans-serif;letter-spacing:1.5px;display:flex;align-items:center;justify-content:center;gap:8px}
.tabs{left:615px;top:958px;width:409px;height:22px;border-bottom:1px solid #ccc;font:500 11.5px "Montserrat",sans-serif;letter-spacing:1.8px;color:#333}
.tabs span{position:absolute;top:0}
.tabs .active::after{content:"";position:absolute;left:0;top:21px;width:100%;height:2px;background:var(--red)}
.description{left:615px;top:1000px;width:415px;font:400 11.7px/20.8px "Montserrat",sans-serif;color:#444}
.description p+p{margin-top:16px}
.share{left:615px;top:1272px;display:flex;gap:9px;align-items:center}
.dot{width:14px;height:14px;border-radius:50%;background:#bbb}

/* related */
.divider{left:0;top:1397px;width:1200px;height:1px;background:var(--line)}
.section-title{left:0;width:1200px;top:1475px;text-align:center;font:700 17px "Montserrat",sans-serif;letter-spacing:4.5px;color:#111}
.card{width:209px;height:265px;border:1px solid #ccc;top:1586px}
.card .photo{position:absolute;inset:20px;background:radial-gradient(circle at 50% 50%,#e6e6e6 0%,#f3f3f3 45%,#fff 75%)}
.card-info{width:209px;top:1869px;text-align:center}
.card-info h3{font:700 14px "Montserrat",sans-serif;letter-spacing:2.5px;color:#111}
.card-info p{font:400 11px "Montserrat",sans-serif;color:#777;margin-top:9px}
.card-info .prices{font:600 10.5px "Montserrat",sans-serif;color:#333;margin-top:6px}
.card-info .prices .off{color:var(--red);font-weight:500}

/* features */
.feature{top:2007px;width:296px;height:153px;border:1px dashed #c8c8c8;text-align:center}
.feature svg{position:absolute;left:50%;top:30px;transform:translateX(-50%)}
.feature h4{position:absolute;left:0;width:100%;top:90px;font:500 11px "Montserrat",sans-serif;letter-spacing:.5px;color:#333}
.feature p{position:absolute;left:0;width:100%;top:111px;font:italic 400 10.5px "Open Sans",sans-serif;color:#555}

/* footer */
.footer{left:0;top:2215px;width:1200px;height:327px;background:var(--footer)}
.footer h5{position:absolute;top:30px;font:500 14.5px "Oswald",sans-serif;color:#fff;letter-spacing:.2px;padding-left:11px;border-left:2px solid var(--teal);line-height:14px;text-transform:uppercase}
.footer ul{position:absolute;top:87px;list-style:none;font:400 11.5px/27.7px "Open Sans",sans-serif;color:var(--footer-text)}
.footer ul li::before{content:"";display:inline-block;width:4px;height:4px;border-radius:50%;background:#777;margin-right:9px;vertical-align:middle}
.footer .contact{left:162px;top:87px;font:400 11.5px/34px "Open Sans",sans-serif;color:var(--footer-text)}
.footer .contact div{display:flex;align-items:center;gap:14px}
.cards{left:152px;top:201px;display:flex;gap:10px}
.cards span{width:27px;height:17px;background:#d8d8d8;border-radius:2px}
.footer-bar{left:0;top:2542px;width:1200px;height:52px;background:var(--footer-bar)}
.footer-bar .copy{position:absolute;left:152px;top:18px;font:400 11.5px "Open Sans",sans-serif;color:var(--footer-text)}
.footer-bar .social{position:absolute;left:944px;top:19px;display:flex;gap:24px}
.footer-bar .social span{width:14px;height:14px;border-radius:50%;background:#8a8a8a}
</style>
</head>
<body>

<div class="abs topbar">
  <span class="abs address">18 Harbor Lane, Kifisia 14561</span>
  <span class="abs phone">Call us -210-555-0142</span>
</div>

<div class="abs search">
  <div class="scope">All
    <svg width="7" height="5" viewBox="0 0 7 5"><path d="M0 0h7L3.5 5z" fill="#333"/></svg>
  </div>
  <div class="field">Search for your categories......
    <svg width="13" height="13" viewBox="0 0 13 13" fill="none" stroke="#999" stroke-width="1.5"><circle cx="5.5" cy="5.5" r="4.5"/><path d="M9 9l3.5 3.5"/></svg>
  </div>
</div>
<a class="abs header-links" style="left:850px">HOME</a>
<a class="abs header-links" style="left:906px">ACCOUNT</a>
<svg class="abs" style="left:980px;top:58px" width="18" height="20" viewBox="0 0 18 20" fill="none" stroke="#333" stroke-width="1.4"><path d="M2 6h14l-1 13H3z"/><path d="M6 8V4a3 3 0 0 1 6 0v4"/></svg>
<div class="abs cart-badge">0</div>
<div class="abs cart-total">$0.00</div>

<div class="abs brand">LAMPIROXA</div>

<nav class="abs main-nav">
  <a class="active" style="left:153px">HANGING</a>
  <i class="sep" style="left:247px"></i>
  <a style="left:265px">ROOF</a>
  <i class="sep" style="left:321px"></i>
  <a style="left:337px">WALL</a>
  <i class="sep" style="left:394px"></i>
  <a style="left:410px">FLOOR</a>
  <i class="sep" style="left:478px"></i>
  <a style="left:498px">SPOT</a>
  <i class="sep" style="left:558px"></i>
  <a style="left:578px">OUTDOOR</a>
  <i class="sep" style="left:674px"></i>
  <a style="left:693px">FANS</a>
  <i class="sep" style="left:756px"></i>
  <a style="left:782px">PROFESSIONAL</a>
  <i class="sep" style="left:928px"></i>
  <a style="left:954px">COMPANY</a>
</nav>

<section class="abs hero" role="img" aria-label="Photo of pendant and table lamps above potted plants and watering cans on a shelf against a blue wall">
  <h1>LOOKING FOR A<br>HOME WITH<br>BEAUTIFUL LIGHTS?</h1>
</section>

<div class="abs breadcrumb"><span>HOME / CATEGORY / <b class="current">PRODUCTS</b></span></div>

<div class="abs main-photo" role="img" aria-label="Product photo of a white LED bulb with screw base"></div>
<svg class="abs arrow" style="left:151px;top:1161px" viewBox="0 0 14 24" fill="none" stroke="#999" stroke-width="1.3"><path d="M11 2L3 12l8 10"/></svg>
<div class="abs thumb" style="left:173px;top:1126px" role="img" aria-label="LED bulb, front view"></div>
<div class="abs thumb" style="left:275px;top:1126px" role="img" aria-label="LED bulb, side view"></div>
<div class="abs thumb" style="left:375px;top:1126px" role="img" aria-label="LED bulb, angled view"></div>
<div class="abs thumb" style="left:476px;top:1126px" role="img" aria-label="LED bulb, tilted view"></div>
<div class="abs thumb" style="left:173px;top:1222px" role="img" aria-label="LED bulb, lying view"></div>
<svg class="abs arrow" style="left:276px;top:1256px" viewBox="0 0 14 24" fill="none" stroke="#999" stroke-width="1.3"><path d="M3 2l8 10-8 10"/></svg>

<h2 class="abs product-title">Lorem Ipsum is simply dummy text of the printing and typesetting industry</h2>
<div class="abs red-rule" style="left:615px;top:787px;width:56px"></div>
<div class="abs price"><span class="cur">$</span><span class="int">199</span><span class="dec">.00</span></div>
<div class="abs qty"><span>QTY</span><i><svg width="7" height="5" viewBox="0 0 7 5" fill="none" stroke="#666"><path d="M.5.5l3 3 3-3"/></svg></i></div>
<a class="abs add-cart">
  <svg width="13" height="13" viewBox="0 0 13 13" fill="none" stroke="#fff" stroke-width="1.3"><circle cx="6.5" cy="6.5" r="5.5"/><path d="M6.5 3.5v6M3.5 6.5h6"/></svg>
  ADD TO CART
</a>

<div class="abs tabs">
  <span class="active" style="left:0">DESCRIPTION</span>
  <span style="left:134px">INFORMATION</span>
  <span style="left:272px">REVIEWS</span>
</div>

<div class="abs description">
  <p>Lorem Ipsum is simply dummy text of the printing and typesetting industry. Lorem Ipsum has been the industry's standard dummy text ever since the 1500s, when an unknown printer took a galley of type and scrambled it to make a type specimen book. It has survived not only five centuries, but also the leap into electronic typesetting, remaining essentially unchanged. It was popularised in the 1960s with the release of Typeleaf sheets containing Lorem Ipsum passages, and more recently with desktop publishing software like Pressline Studio including versions of Lorem Ipsum.</p>
  <p>Lorem Ipsum is simply dummy text of the printing and typesetting industry. Lorem Ipsum has been the industry's standard dummy text</p>
</div>

<div class="abs share">
  <svg width="20" height="20" viewBox="0 0 20 20" fill="none" stroke="#888" stroke-width="1.3"><circle cx="4" cy="10" r="2.5"/><circle cx="16" cy="4" r="2.5"/><circle cx="16" cy="16" r="2.5"/><path d="M6.2 8.8l7.6-3.6M6.2 11.2l7.6 3.6"/></svg>
  <i class="dot" style="margin-left:6px"></i><i class="dot"></i><i class="dot"></i><i class="dot"></i><i class="dot" style="margin-left:8px"></i>
</div>

<div class="abs divider"></div>
<h2 class="abs section-title">RELATED PRODUCTS</h2>
<div class="abs red-rule" style="left:570px;top:1517px;width:60px"></div>

<svg class="abs arrow" style="left:233px;top:1674px" viewBox="0 0 14 24" fill="none" stroke="#555" stroke-width="1.5"><path d="M11 2L3 12l8 10"/></svg>
<div class="abs card" style="left:261px"><div class="photo" role="img" aria-label="White LED bulb"></div></div>
<div class="abs card" style="left:495px"><div class="photo" role="img" aria-label="Metal LED power supply unit"></div></div>
<div class="abs card" style="left:728px"><div class="photo" role="img" aria-label="Aluminium LED strip profile"></div></div>
<svg class="abs arrow" style="left:957px;top:1674px" viewBox="0 0 14 24" fill="none" stroke="#555" stroke-width="1.5"><path d="M3 2l8 10-8 10"/></svg>

<div class="abs card-info" style="left:261px"><h3>LOREM IPSUM</h3><p>lorem Ipsum is simply</p><div class="prices">$ 2,000 &nbsp; $ 900 &nbsp; <span class="off">(40% Off)</span></div></div>
<div class="abs card-info" style="left:495px"><h3>LOREM IPSUM</h3><p>lorem Ipsum is simply</p><div class="prices">$ 2,000 &nbsp; $ 900 &nbsp; <span class="off">(40% Off)</span></div></div>
<div class="abs card-info" style="left:728px;top:1866px"><h3>LOREM IPSUM</h3><p>lorem Ipsum is simply</p><div class="prices">$ 2,000 &nbsp; $ 900 &nbsp; <span class="off">(40% Off)</span></div></div>

<div class="abs feature" style="left:130px">
  <svg width="30" height="34" viewBox="0 0 30 34" fill="none" stroke="#777" stroke-width="1.3"><circle cx="15" cy="14" r="11"/><path d="M4 14h22M15 3c-5 6-5 16 0 22M15 3c5 6 5 16 0 22M9 31h12M15 25v6"/></svg>
  <h4>FREE SHIPPING WORLDWIDE</h4><p>Free shipping worldwide</p>
</div>
<div class="abs feature" style="left:451px">
  <svg width="34" height="34" viewBox="0 0 34 34" fill="none" stroke="#777" stroke-width="1.3"><path d="M6 19v-3a11 11 0 0 1 22 0v3"/><rect x="4" y="18" width="5" height="9" rx="2"/><rect x="25" y="18" width="5" height="9" rx="2"/><path d="M27.5 27c0 3-3 4-7 4"/></svg>
  <h4>24/7 CUSTOMER SERVICE</h4><p>Service Support 24/7</p>
</div>
<div class="abs feature" style="left:771px">
  <svg width="34" height="34" viewBox="0 0 34 34" fill="none" stroke="#777" stroke-width="1.3"><path d="M27 13A11 11 0 0 0 7 11M7 21a11 11 0 0 0 20 2"/><path d="M7 5v6h6M27 29v-6h-6"/></svg>
  <h4>MONEY BACK GUARANTEE!100%</h4><p>Money Back – 30 Days</p>
</div>

<footer class="abs footer">
  <h5 style="left:152px">About Store</h5>
  <h5 style="left:410px">My Account</h5>
  <h5 style="left:669px">Information</h5>
  <h5 style="left:929px">Customer Service</h5>

  <div class="abs contact">
    <div><svg width="12" height="11" viewBox="0 0 12 11" fill="#aaa"><path d="M6 0l6 5.5h-2V11H7.5V7.5h-3V11H2V5.5H0z"/></svg>77 Olive Grove Rd, Marousi</div>
    <div><svg width="12" height="12" viewBox="0 0 12 12" fill="#aaa"><path d="M2.5 0l2 3-1.3 1.5a7 7 0 0 0 4.3 4.3L9 7.5l3 2-1.3 2.2C5 12 0 7 .3 1.3z"/></svg>(800) 555 0199</div>
    <div><svg width="12" height="10" viewBox="0 0 12 10" fill="none" stroke="#aaa" stroke-width="1.2"><rect x=".6" y=".6" width="10.8" height="8.8"/><path d="M.6.6L6 5.5 11.4.6"/></svg>contact@brightshop.com</div>
  </div>
  <div class="abs cards"><span></span><span></span><span></span><span></span><span></span></div>

  <ul style="left:410px"><li>My Account</li><li>Wishlist</li><li>My Cart</li><li>Checkout</li></ul>
  <ul style="left:669px"><li>About Us</li><li>Careers</li><li>Delivery Information</li><li>Privacy Policy</li><li>Terms &amp; Condition</li><li>Sale products</li></ul>
  <ul style="left:929px"><li>Shipping Policy</li><li>Compensation First</li><li>My Account</li><li>Return Policy</li><li>Contact Us</li><li>Shipping Info</li></ul>
</footer>

<div class="abs footer-bar">
  <span class="copy">Copyright © 2016</span>
  <div class="social"><span></span><span></span><span></span><span></span><span></span></div>
</div>

</body>
</html>
```